Top Producing Realtor Business Card Design

Looking for branding with my logo on all of my materials. I am a top producing real estate agent, selling expensive homes in California. I'm looking for a classy design that includes my existing logo, the company corporate logo and my photo.

Looking forward to your submissions! Thank you so much! :)

I appreciate your submissions very much!  Excellent work!  I have revised the brief to be more clear about what I think I'm looking for.  Keep the submissions coming in!!  Thank you so much :)

Target Market(s)

Wealthy home buyers and sellers in California.

Industry/Entity Type

Real Estate

Requirements
Must have
• Must include:

Homestead Pinnacle Logo

Below Homestead Pinnacle Logo it must say: Santa Clarita (Helvetica font)

Complete address: 58317 Barwick Street
Santa Clarita, CA 94687

Phone number: 415.962.3057 cell
415.740.2195 VM 5821 office

My photo

My name: Mara Quinlow (please make sure it's correct before you submit) :)

My MQ Logo (if possible please keep logo colors the same)

"Realtor" with a reserved symbol after or below my name

My license number: StaREB #07428915

My website: www.MaraQuinlow-example.com

My email: Mara@MaraQuinlow-example.com

Nice to have
• I'm open minded :) The main goal is to have the MQ logo is on all of my material. For the business cards I sort of imagine my MQ logo in the background, and I like a fade. I prefer the logo to be on the front of the card, and I like it on the back of the card too, So a two sided business card is ok.

I prefer the light blue Homestead Pinnacle Logo submitted. Please note the light blue color must closely match :)

Another idea is the business card can be in the format of the yard sign photo submitted (maybe changed into the light blue color), to possibly be a business card that looks like the yard sign. The yard sign layout must closely match the example submitted due to corporate guidelines.

Basically I'm looking for something that will tie everything together with my photo and logo so it's well branded in the clients mind. :)

Should not have
• Please keep the logo's exactly as they are, including color...no need to change.

If you choose to use the yard sign example provided for the business card, Please do not change the basic layout of the yard sign submitted, I have to follow the corporate standards.

```html
<!DOCTYPE html>
<html lang="en">
<head>
<meta charset="utf-8">
<title>Mara Quinlow – Business Card</title>
<link rel="stylesheet" href="https://fonts.googleapis.com/css2?family=Arimo:wght@400;700&family=Montserrat:wght@400;600&display=swap">
<style>
  :root {
    --card-blue: #1f4f99;
    --mark-blue: #2a6bc9;
    --ink-white: #ffffff;
    --mark-light: #dde5f1;
    --page: #ffffff;
    --photo-light: #a9a9a6;
    --photo-dark: #3b3b3b;
  }
  html, body {
    margin: 0;
    padding: 0;
    width: 1034px;
    height: 1200px;
    overflow: hidden;
    background: var(--page);
  }
  .canvas {
    position: relative;
    width: 1034px;
    height: 1200px;
    font-family: "Arimo", Helvetica, Arial, sans-serif;
    color: var(--ink-white);
  }
  .card {
    position: absolute;
    left: 6px;
    width: 1028px;
    background: var(--card-blue);
    overflow: hidden;
  }
  .card--front { top: 0; height: 585px; }
  .card--back { top: 614px; height: 586px; left: 0; width: 1034px; }

  .brokerage {
    position: absolute;
    left: 58px;
    top: 52px;
    width: 280px;
    height: 150px;
    display: flex;
    flex-direction: column;
    align-items: center;
    justify-content: center;
    gap: 6px;
  }
  .brokerage__badge {
    width: 18px;
    height: 18px;
    background: var(--ink-white);
  }
  .brokerage__name {
    font-family: "Arimo", Helvetica, Arial, sans-serif;
    font-weight: 700;
    font-size: 28px;
    line-height: 1.1;
    text-align: center;
    color: var(--ink-white);
  }
  .brokerage__city {
    position: absolute;
    left: 58px;
    width: 280px;
    top: 207px;
    text-align: center;
    font-weight: 700;
    font-size: 15px;
  }
  .agent-mark {
    position: absolute;
    left: 378px;
    top: 70px;
    width: 160px;
    text-align: center;
    font-family: "Montserrat", sans-serif;
    font-weight: 600;
    font-size: 78px;
    color: var(--mark-light);
  }
  .identity {
    position: absolute;
    left: 0;
    width: 550px;
    top: 242px;
    text-align: center;
  }
  .identity__name {
    font-family: "Montserrat", sans-serif;
    font-weight: 600;
    font-size: 33px;
    line-height: 40px;
  }
  .identity__title {
    font-family: "Montserrat", sans-serif;
    font-weight: 400;
    font-size: 21px;
    letter-spacing: 0.5px;
    line-height: 26px;
  }
  .identity__title sup { font-size: 9px; vertical-align: 10px; }
  .identity__license {
    font-weight: 700;
    font-size: 17px;
    line-height: 26px;
  }
  .contacts {
    position: absolute;
    left: 70px;
    top: 366px;
    margin: 0;
    padding: 0;
    list-style: none;
  }
  .contacts__item {
    position: absolute;
    left: 0;
    display: flex;
    align-items: center;
    white-space: nowrap;
    font-weight: 700;
    font-size: 17px;
  }
  .contacts__icon {
    width: 34px;
    height: 30px;
    margin-right: 14px;
    flex: none;
  }
  .photo {
    position: absolute;
    left: 558px;
    top: 0;
    width: 470px;
    height: 585px;
    background: radial-gradient(ellipse at 50% 35%, var(--photo-light), var(--photo-dark) 85%);
  }

  .back-mark {
    position: absolute;
    left: 20px;
    bottom: -150px;
    font-family: "Montserrat", sans-serif;
    font-weight: 600;
    font-size: 520px;
    line-height: 1;
    color: var(--mark-blue);
    letter-spacing: -20px;
  }
  .back-identity {
    position: absolute;
    left: 560px;
    width: 350px;
    top: 272px;
    text-align: center;
  }
  .back-identity__name {
    font-family: "Montserrat", sans-serif;
    font-weight: 600;
    font-size: 42px;
    line-height: 48px;
  }
  .back-identity__title {
    font-family: "Montserrat", sans-serif;
    font-weight: 400;
    font-size: 25px;
    line-height: 30px;
    letter-spacing: 0.5px;
  }
  .back-identity__title sup { font-size: 10px; vertical-align: 12px; }
</style>
</head>
<body>
<main class="canvas">

  <section class="card card--front">
    <div class="brokerage">
      <span class="brokerage__badge"></span>
      <span class="brokerage__name">Homestead<br>Pinnacle</span>
    </div>
    <div class="brokerage__city">Santa Clarita</div>

    <div class="agent-mark">MQ</div>

    <div class="identity">
      <div class="identity__name">Mara Quinlow</div>
      <div class="identity__title">REALTOR<sup>®</sup></div>
      <div class="identity__license">StaREB #07428915</div>
    </div>

    <ul class="contacts">
      <li class="contacts__item" style="top:0">
        <svg class="contacts__icon" viewBox="0 0 34 30"><path d="M17 2a8 8 0 0 0-8 8c0 6 8 17 8 17s8-11 8-17a8 8 0 0 0-8-8zm0 11a3 3 0 1 1 0-6 3 3 0 0 1 0 6z" fill="#fff"/></svg>
        58317 Barwick Street, Santa Clarita, CA 94687
      </li>
      <li class="contacts__item" style="top:47px">
        <svg class="contacts__icon" viewBox="0 0 34 30"><path d="M13 3c-3 1-4 4-4 11s1 12 4 13l3-1-1-7-3 1c-1-2-1-10 0-12l3 1 1-6z" fill="#fff"/></svg>
        415.740.2195 VM 5821
      </li>
      <li class="contacts__item" style="top:89px">
        <svg class="contacts__icon" viewBox="0 0 34 30"><rect x="11" y="3" width="12" height="25" rx="2" fill="#fff"/><rect x="13" y="6" width="8" height="7" fill="#1f4f99"/><g fill="#1f4f99"><rect x="13" y="16" width="2" height="2"/><rect x="16" y="16" width="2" height="2"/><rect x="19" y="16" width="2" height="2"/><rect x="13" y="20" width="2" height="2"/><rect x="16" y="20" width="2" height="2"/><rect x="19" y="20" width="2" height="2"/></g><rect x="12" y="0" width="2" height="4" fill="#fff"/></svg>
        415.962.3057
      </li>
      <li class="contacts__item" style="top:121px">
        <svg class="contacts__icon" viewBox="0 0 34 30"><rect x="1" y="7" width="32" height="18" fill="#fff"/><path d="M1 7l16 11 16-11M1 25l12-9M33 25l-12-9" stroke="#1f4f99" stroke-width="2" fill="none"/></svg>
        Mara@MaraQuinlow-example.com
      </li>
      <li class="contacts__item" style="top:160px">
        <svg class="contacts__icon" viewBox="0 0 34 30"><circle cx="17" cy="15" r="13" fill="#fff"/><g stroke="#1f4f99" stroke-width="1.5" fill="none"><ellipse cx="17" cy="15" rx="6" ry="13"/><path d="M4 15h26M6 8h22M6 22h22M17 2v26"/></g></svg>
        www.MaraQuinlow-example.com
      </li>
    </ul>

    <div class="photo" role="img" aria-label="Portrait photo of Mara Quinlow in a dark blazer and white shirt against a grey studio backdrop"></div>
  </section>

  <section class="card card--back">
    <div class="back-mark">MQ</div>
    <div class="back-identity">
      <div class="back-identity__name">Mara Quinlow</div>
      <div class="back-identity__title">REALTOR<sup>®</sup></div>
    </div>
  </section>

</main>
</body>
</html>
```